Webdesign
Zielgruppe
Briefing für die neue Website von TELORI GmbH
Allgemeine Informationen:
Name des Unternehmens: TELORI GmbH
Branche: Maschinenbau
Zweck der Website: Eine Unternehmenswebsite, die informiert, was die Firma macht und es potenziellen Kunden oder Partnern ermöglicht, in Kontakt zu treten.
Zielgruppe:
Hauptzielgruppe: Anlagenbauer, Maschinenbauer, Anlagenbetreiber aus verschiedenen Branchen.
Design-Anforderungen: Die Zielgruppe erwartet Professionalität und Klarheit, also sollte die Website eine hohe Qualität, Professionalität und Benutzerfreundlichkeit reflektieren.
Design-Vorlieben:
Farbschema & Stil: Das Design sollte sich an den bereitgestellten Logos orientieren. Der gewünschte Stil ist modern und klar.
Inspirationsquellen: Die Logos des Unternehmens, die dem Briefing beigefügt werden.
Inhalt und Struktur:
Einseitiges Design: Die Website sollte nur eine Seite zum Herunterscrollen haben.
Unternehmensvorstellung: Ein kurzer Abschnitt, der beschreibt, wer TELORI GmbH ist und was das Unternehmen macht.
Leistungsübersicht: Eine klare Darstellung der Dienstleistungen oder Produkte, die TELORI GmbH anbietet. Dies kann durch Symbole, kurze Texte oder Bilder dargestellt werden.
Kontaktmöglichkeit: Ein Kontaktformular oder zumindest klare Kontaktinformationen (Telefon, E-Mail, Adresse), so dass Besucher leicht in Kontakt treten können.
Aufgabenstellung
siehe oben

```html
<!DOCTYPE html>
<html lang="de">
<head>
<meta charset="utf-8">
<title>TELORI GmbH – Maschinenbau</title>
<link rel="stylesheet" href="https://fonts.googleapis.com/css2?family=Montserrat:wght@400;500;700&family=Saira+Extra+Condensed:wght@600;700&family=Oswald:wght@600&display=swap">
<style>
:root{
  --dark:#333333;
  --white:#ffffff;
  --red:#c0050f;
  --field:#6b6b6b;
  --ink:#2f2f2f;
  --muted:#555555;
}
*{box-sizing:border-box;margin:0;padding:0}
html,body{width:1200px;height:3280px;overflow:hidden}
body{font-family:"Montserrat",sans-serif;background:var(--white);color:var(--ink)}
.page{position:relative;width:1200px;height:3280px}
section,footer{position:absolute;left:0;width:1200px}
.heading{font-family:"Saira Extra Condensed","Oswald","Arial Narrow",sans-serif;font-weight:700;font-stretch:condensed;text-transform:uppercase;line-height:1;letter-spacing:-0.5px;white-space:nowrap}
.hero{top:0;height:460px;background:linear-gradient(100deg,#1d2a38 0%,#2c3b4a 35%,#6a5a2e 70%,#b08a2a 100%);color:var(--white)}
.hero .visual{position:absolute;inset:0}
.hero-title{position:absolute;left:114px;top:40px;font-size:46px}
.hero-text{position:absolute;left:114px;top:200px;width:420px;font-size:25px;line-height:23px}
.hero-brand{position:absolute;left:662px;top:196px;width:370px;text-align:center;font-family:"Montserrat",sans-serif;font-weight:700;font-size:54px;letter-spacing:2px;color:var(--white);white-space:nowrap}
.service{height:451px}
.service.dark{background:var(--dark);color:var(--white)}
.service.light{background:var(--white);color:var(--ink)}
.service .photo{position:absolute;top:80px;width:400px;height:290px}
.service .copy{position:absolute;top:78px;width:530px}
.service .copy h2{font-size:48px;margin-bottom:12px}
.service .copy p{font-size:25px;line-height:25px}
.service .copy .ask{margin-top:12px;font-weight:500}
.btn{display:inline-block;width:236px;height:40px;margin-top:24px;border-radius:10px;background:var(--red);color:var(--white);font-weight:700;font-size:20px;line-height:40px;text-align:center}
.contact{top:2261px;height:789px;background:var(--dark);color:var(--white)}
.contact h2{position:absolute;left:114px;top:80px;font-size:46px}
.field{position:absolute;left:114px;width:646px;height:55px;border-radius:8px;background:var(--field);font-size:26px;line-height:55px;padding-left:18px}
.field.message{height:214px;line-height:1;padding-top:16px}
.contact .btn{position:absolute;left:114px;top:667px;margin:0}
.contact-data{position:absolute;right:114px;top:236px;width:320px;text-align:right}
.contact-data h3{color:var(--red);font-size:42px;margin-bottom:18px}
.contact-data li{list-style:none;position:relative;font-size:20px;line-height:36px}
.contact-data svg{position:absolute;left:0;top:8px}
.site-footer{top:3050px;height:230px;background:var(--white)}
.footer-brand{position:absolute;left:114px;top:85px;font-weight:700;font-size:34px;color:var(--red);letter-spacing:1px;white-space:nowrap}
.footer-contact{position:absolute;left:441px;top:44px;font-size:20px;line-height:29px;color:var(--muted)}
.footer-hours{position:absolute;left:768px;top:79px;font-size:20px;line-height:29px;color:var(--muted)}
.legal-bar{position:absolute;left:0;top:196px;width:1200px;height:34px;background:var(--dark);color:var(--white);font-size:10px;line-height:34px}
.legal-bar span{position:absolute}
</style>
</head>
<body>
<div class="page">

  <section class="hero">
    <div class="visual" role="img" aria-label="Industriehalle mit gelben Roboterarmen und digitalen Symbolen"></div>
    <h1 class="hero-title heading">Herzlich<br>Willkommen!</h1>
    <p class="hero-text">Hier soll ein Kurzer Abschnitt entstehen, der beschreibt, wer TELORI GmbH ist und was das Unternehmen macht.</p>
    <div class="hero-brand">TELORI GmbH</div>
  </section>

  <section class="service dark" style="top:460px">
    <div class="photo" style="left:114px;background:linear-gradient(135deg,#9fb4c0,#2f8db0 55%,#5e6a70)" role="img" aria-label="Blaue Elektromotoren an einer Pumpenanlage"></div>
    <div class="copy" style="left:564px">
      <h2 class="heading">Leistungsbereich 1</h2>
      <p>Hier wird der erste Leistungsbereich kurz beschrieben, um das Interesse des Kunden zu wecken und zum Kontaktformular zu gehen um eine Zusammenarbeit anzufragen.</p>
      <p class="ask">Sie sind Interessiert?</p>
      <span class="btn">Jetzt anfragen</span>
    </div>
  </section>

  <section class="service light" style="top:910px">
    <div class="copy" style="left:114px;width:545px">
      <h2 class="heading">Leistungsbereich 2</h2>
      <p>Hier wird der zweite Leistungsbereich kurz beschrieben, um das Interesse des Kunden zu wecken und zum Kontaktformular zu gehen um eine Zusammenarbeit anzufragen.</p>
      <p class="ask">Sie sind Interessiert?</p>
      <span class="btn">Jetzt anfragen</span>
    </div>
    <div class="photo" style="left:687px;background:linear-gradient(160deg,#d8dde0,#8e979c 60%,#3c4448)" role="img" aria-label="Abfüllanlage mit Förderbändern in einer hellen Halle"></div>
  </section>

  <section class="service dark" style="top:1361px">
    <div class="photo" style="left:114px;background:linear-gradient(135deg,#c9ccc8,#b0683a 45%,#6e7a6e)" role="img" aria-label="Fertigungsstraße mit orangefarbenen Industrierobotern"></div>
    <div class="copy" style="left:564px">
      <h2 class="heading">Leistungsbereich 3</h2>
      <p>Hier wird der erste Leistungsbereich kurz beschrieben, um das Interesse des Kunden zu wecken und zum Kontaktformular zu gehen um eine Zusammenarbeit anzufragen.</p>
      <p class="ask">Sie sind Interessiert?</p>
      <span class="btn">Jetzt anfragen</span>
    </div>
  </section>

  <section class="service light" style="top:1811px">
    <div class="copy" style="left:114px;width:545px">
      <h2 class="heading">Leistungsbereich 4</h2>
      <p>Hier wird der zweite Leistungsbereich kurz beschrieben, um das Interesse des Kunden zu wecken und zum Kontaktformular zu gehen um eine Zusammenarbeit anzufragen.</p>
      <p class="ask">Sie sind Interessiert?</p>
      <span class="btn">Jetzt anfragen</span>
    </div>
    <div class="photo" style="left:688px;background:linear-gradient(135deg,#2a3038,#3a7fb8 50%,#9aa2a8)" role="img" aria-label="Montageautomat mit blauen Pneumatikschläuchen"></div>
  </section>

  <section class="contact">
    <h2 class="heading">Nehmen Sie Kontakt auf</h2>
    <div class="field" style="top:172px">Name</div>
    <div class="field" style="top:246px">Vorname</div>
    <div class="field" style="top:323px;padding-left:14px">E-Mail</div>
    <div class="field message" style="top:396px;padding-left:14px">Ihre Nachricht</div>
    <span class="btn">Senden</span>

    <div class="contact-data">
      <h3 class="heading">Unsere<br>Kontaktdaten</h3>
      <ul>
        <li><svg width="24" height="20" viewBox="0 0 24 20" fill="none" stroke="#fff" stroke-width="1.6"><rect x="1" y="2" width="20" height="15" rx="1"/><path d="M1 3l10 8 10-8"/></svg>kontakt@telori-werk.de</li>
        <li><svg width="22" height="22" viewBox="0 0 24 24" fill="none" stroke="#fff" stroke-width="1.6"><path d="M5 2h4l2 5-3 2a12 12 0 0 0 7 7l2-3 5 2v4a2 2 0 0 1-2 2A19 19 0 0 1 3 4a2 2 0 0 1 2-2z"/></svg>+49 30 5549 8172</li>
        <li><svg width="22" height="22" viewBox="0 0 24 24" fill="none" stroke="#fff" stroke-width="1.6"><path d="M3 11l9-8 9 8M5 9v12h5v-6h4v6h5V9"/></svg>Lindenweg 7</li>
        <li>54321 Beispielstadt</li>
      </ul>
    </div>
  </section>

  <footer class="site-footer">
    <div class="footer-brand">TELORI GmbH</div>
    <div class="footer-contact">kontakt@telori-werk.de<br>+49 30 5549 8172<br>Lindenweg 7<br>54321 Beispielstadt</div>
    <div class="footer-hours">Öffnungszeiten<br>Mo-Fr:</div>
    <div class="legal-bar">
      <span style="left:114px;font-weight:700">© 2023 – COPYRight</span>
      <span style="left:768px">Impressum</span>
      <span style="left:932px">Datenschutz</span>
    </div>
  </footer>

</div>
</body>
</html>
```